wedding photography website for top wedding photographer

I have a website right now that is barely working. I want the photos to maybe all the photos lined up horizontally and you scroll to see the images. I have an orange logo and want it to be dark grey. I also need a page for publications (I have those as scans) and a link to an About page.

Target Market(s)

wedding planners and bride

Industry/Entity Type

Wedding Photography

Coding

Coded - Design and coding required

Number of Pages Required

5+ page

Font styles to use
Serif
Sans Serif

Colors
ffffff
474747

Requirements
Must have
• easy to navigate, always want the instagram and contact info readily available, should be clean and modern and let the photos stand out. it's wedding photos but i don't want it to feel girly or prissy.
Nice to have
• possibly could be one big photo on the home page, then click it to go into all the other photos. want page options on the home page and every page
Should not have
• nothing fussy or quaint, want this to be the "Copper Ladle" restaurant of wedding photography

```html
<!DOCTYPE html>
<html lang="en">
<head>
<meta charset="utf-8">
<title>Ivory Lane Photography</title>
<link href="https://fonts.googleapis.com/css2?family=Open+Sans:wght@400;600&family=Raleway:wght@300;400&display=swap" rel="stylesheet">
<style>
  :root {
    --accent: #474747;
    --ink: #474747;
    --muted: #8a8a8a;
    --white: #ffffff;
    --paper: #f4f4f4;
    --line: #e4e4e4;
    --panel: #1d1d1d;
  }
  * { box-sizing: border-box; margin: 0; padding: 0; }
  html, body { width: 795px; height: 1200px; overflow: hidden; }
  body {
    position: relative;
    background: var(--white);
    font-family: "Open Sans", Arial, sans-serif;
    color: var(--ink);
  }
  .abs { position: absolute; }

  .backdrop {
    left: 0; top: 0; width: 795px; height: 500px;
    background:
      radial-gradient(ellipse at 85% 20%, rgba(170,170,170,.45), transparent 55%),
      radial-gradient(ellipse at 10% 30%, rgba(190,190,190,.4), transparent 50%),
      linear-gradient(180deg, #e6e6e6 0%, #f1f1f1 55%, #ffffff 100%);
  }

  .topbar {
    left: 0; top: 0; width: 795px; height: 19px;
    background: rgba(255,255,255,.85);
    border-bottom: 1px solid var(--line);
  }
  .social { left: 158px; top: 4px; display: flex; gap: 4px; }
  .social span { width: 11px; height: 11px; background: #cfcfcf; border-radius: 1px; }
  .nav { right: 0; top: 0; display: flex; height: 19px; }
  .nav a {
    display: block; padding: 0 9px; line-height: 19px;
    font-size: 7px; color: var(--ink); text-decoration: none;
  }
  .nav a.active { background: var(--accent); color: var(--white); }

  .brand {
    left: 0; width: 795px; top: 32px; text-align: center;
    font-family: "Raleway", Arial, sans-serif; font-weight: 400;
    font-size: 20px; line-height: 26px; color: var(--ink); letter-spacing: .5px;
  }

  /* Horizontal gallery: one photo in view, the rest scroll sideways */
  .gallery {
    left: 156px; top: 72px; width: 483px; height: 198px;
    display: flex; overflow-x: auto; overflow-y: hidden;
    scroll-snap-type: x mandatory; scrollbar-width: none;
  }
  .gallery::-webkit-scrollbar { display: none; }
  .gallery-item { flex: 0 0 483px; height: 198px; scroll-snap-align: start; }
  .item-dance {
    background:
      radial-gradient(ellipse at 50% 62%, #4e4646 0 16%, transparent 34%),
      radial-gradient(circle at 15% 30%, #d7c8d4, transparent 42%),
      radial-gradient(circle at 85% 70%, #c8bccd, transparent 42%),
      linear-gradient(135deg, #ad9caa, #e6dde3 50%, #9a8ea0);
  }
  .item-field { background: linear-gradient(135deg, #8a6a3c, #d9bf8e 55%, #6b4e2c); }
  .item-venue { background: linear-gradient(135deg, #6f7a86, #dfe4ea 55%, #5a6470); }

  .about {
    left: 156px; top: 270px; width: 483px; height: 186px;
    background: var(--white);
    text-align: center;
    box-shadow: 0 2px 6px rgba(0,0,0,.06);
  }
  .section-title {
    font-family: "Raleway", Arial, sans-serif; font-weight: 300;
    color: var(--ink); font-size: 18px; line-height: 22px;
  }
  .about .section-title { margin-top: 28px; }
  .about p {
    width: 360px; margin: 10px auto 0;
    font-size: 6.4px; line-height: 10px; color: var(--muted);
  }
  .btn {
    display: inline-block; background: var(--accent); color: var(--white);
    font-size: 7px; border-radius: 9px; padding: 0 16px; line-height: 16px;
  }
  .about .btn { margin-top: 10px; }
  .note-band {
    left: 236px; top: 434px; width: 323px; height: 24px;
    background: var(--paper); border-radius: 12px;
    font-size: 5.5px; line-height: 8px; color: var(--muted);
    text-align: center; padding-top: 4px;
  }

  .feature-photo {
    background:
      radial-gradient(ellipse at 50% 55%, #3a3a44 0 14%, transparent 28%),
      radial-gradient(circle at 20% 30%, #a8cfe8, transparent 45%),
      radial-gradient(circle at 80% 35%, #c4bfdc, transparent 45%),
      linear-gradient(135deg, #79a9cf, #eaf2f8 55%, #94b2d8);
    border: 5px solid var(--white);
    box-shadow: 0 0 0 1px var(--line), 0 2px 5px rgba(0,0,0,.08);
  }
  .photo-one { left: 158px; top: 503px; width: 235px; height: 153px; }
  .photo-two { left: 398px; top: 694px; width: 240px; height: 154px; }

  .feature-copy { width: 225px; }
  .feature-copy h3 {
    font-family: "Open Sans", Arial, sans-serif; font-weight: 400;
    font-size: 10px; line-height: 14px; color: var(--ink);
  }
  .feature-copy p {
    margin-top: 8px; font-size: 6.2px; line-height: 9.5px; color: var(--muted);
  }
  .feature-copy .btn { margin-top: 12px; }
  .copy-one { left: 410px; top: 531px; }
  .copy-two { left: 158px; top: 709px; }

  .newsletter-band {
    left: 0; top: 882px; width: 795px; height: 227px;
    background:
      radial-gradient(ellipse at 25% 55%, #d9c3a0 0 12%, transparent 30%),
      radial-gradient(ellipse at 15% 20%, #f3d79c, transparent 40%),
      linear-gradient(180deg, #6b4e2c 0%, #a7824d 45%, #c9a466 70%, #8a6a3c 100%);
  }
  .newsletter {
    left: 339px; top: 927px; width: 297px; height: 133px;
    background: rgba(20,20,20,.82);
    padding: 16px 26px;
  }
  .newsletter h2 {
    font-family: "Raleway", Arial, sans-serif; font-weight: 300;
    font-size: 22px; line-height: 26px; color: var(--white);
  }
  .newsletter p { margin-top: 6px; font-size: 6px; line-height: 9px; color: #bdbdbd; width: 220px; }
  .newsletter .field {
    margin-top: 7px; width: 190px; height: 14px; background: var(--white);
    font-size: 6px; line-height: 14px; padding-left: 6px; color: #a0a0a0; border-radius: 2px;
  }
  .newsletter .btn {
    margin-top: 7px; border-radius: 2px; padding: 0 18px;
    background: var(--white); color: var(--ink);
  }

  .footer {
    left: 0; top: 1109px; width: 795px; height: 91px;
    background: var(--paper); text-align: center;
  }
  .footer p {
    width: 400px; margin: 16px auto 0; font-size: 6px; line-height: 9px; color: var(--muted);
  }
  .footer .copyright { margin-top: 22px; font-size: 5.5px; }
</style>
</head>
<body>
  <div class="abs backdrop" role="img" aria-label="Soft faded wedding photograph of a bride and groom behind the page"></div>

  <header class="abs topbar">
    <div class="abs social"><span></span><span></span><span></span></div>
    <nav class="abs nav">
      <a class="active" href="#">Home</a>
      <a href="#">About</a>
      <a href="#">Portfolio</a>
      <a href="#">Video</a>
      <a href="#">Contact</a>
    </nav>
  </header>

  <div class="abs brand">Ivory Lane Photography</div>

  <div class="abs gallery" aria-label="Photo gallery, scroll sideways">
    <div class="gallery-item item-dance" role="img" aria-label="Bride and groom dancing in front of a sparkling floral backdrop"></div>
    <div class="gallery-item item-field" role="img" aria-label="Couple embracing in a golden field"></div>
    <div class="gallery-item item-venue" role="img" aria-label="Wedding reception hall in soft evening light"></div>
  </div>

  <section class="abs about">
    <h2 class="section-title">About Us</h2>
    <p>Every wedding tells its own story, and we are there to capture it honestly. We work quietly beside you through the day, finding the small moments between the big ones. Our approach is calm, natural and unposed, so the photographs feel like you rather than a set piece. From the first look to the last dance, every frame is edited by hand and delivered in a gallery made to last for years.</p>
    <span class="btn">Read More</span>
  </section>
  <div class="abs note-band">Booking now for the coming season.<br>Get in touch early to reserve your date.</div>

  <div class="abs feature-photo photo-one" role="img" aria-label="Couple seen from behind facing a glowing bokeh backdrop"></div>
  <div class="abs feature-copy copy-one">
    <h3>Wedding photography</h3>
    <p>Relaxed, documentary coverage of your whole day, from getting ready to the final send-off. Every image is colour graded by hand for a clean and timeless finish.</p>
    <span class="btn">View More</span>
  </div>

  <div class="abs feature-copy copy-two">
    <h3>Wedding photography</h3>
    <p>Portraits of the two of you in soft evening light, made without stiff poses. We guide gently and let the real moments between you come through.</p>
    <span class="btn">View More</span>
  </div>
  <div class="abs feature-photo photo-two" role="img" aria-label="Couple seen from behind facing a glowing bokeh backdrop"></div>

  <div class="abs newsletter-band" role="img" aria-label="Bride and groom embracing in a golden field at sunset"></div>
  <section class="abs newsletter">
    <h2>Join Our Newsletter</h2>
    <p>Sign up for seasonal news, new galleries and booking dates.</p>
    <div class="field">Your email address</div>
    <span class="btn">Submit</span>
  </section>

  <footer class="abs footer">
    <p>Ivory Lane Photography covers weddings across the region and beyond. For availability, packages and collections, send a short note with your date and venue and we will reply within two working days.</p>
    <p class="copyright">Copyright © 2024 Ivory Lane Photography</p>
  </footer>
</body>
</html>
```